Business Card Design For DJ Company

I'm rebranding my wedding and event dj company. I am looking for a modern, luxury, & fun design to match my new logo and website design. Please see attached logo and new webpage design. Colors should match. Design should flow with logo and website for recognition. I want to attract young adults. I plan on printing metallic finish cards so please keep hat in mind.

Target Market(s)

Millennials

Contact Information for Business Card

Name: Dario Velloza
Company: Coral Tide Fiesta DJ
Services: DJ – Photo Booth – Event Lighting – LED Robot

Website: www.coraltidefiestadj.example
Email: dario@coraltidefiestadj.example
Phone: (555)014-7392

Instagram: @ctfiestadj
Facebook: @ctfiestadj
Twitter - @ctfiestadj

Se Habla Español

Font styles to use
Serif
Sans Serif

Colors

Designer to choose colors to be used in the design.

Requirements
Nice to have
• Transparent Gradient background - Image related to weddings

```html
<!DOCTYPE html>
<html lang="en">
<head>
<meta charset="utf-8">
<title>Coral Tide Fiesta DJ – Business Card</title>
<link href="https://fonts.googleapis.com/css2?family=Lato:wght@400;700&family=Michroma&display=swap" rel="stylesheet">
<style>
  :root{
    --orange:#f7941d;
    --green:#8dc63f;
    --blue:#29a8e0;
    --ink:#2b2b2b;
    --black:#000;
    --white:#fff;
    --stage:#e9e4dc;
    --rule:#9a9a9a;
  }
  *{margin:0;padding:0;box-sizing:border-box}
  html,body{width:1200px;height:1093px;overflow:hidden}
  body{background:var(--stage);position:relative;font-family:"Lato",sans-serif}
  .card{position:absolute;width:800px;height:456px;border-radius:46px;overflow:hidden}
  .card-front{left:323px;top:57px;background:var(--white);border:2px solid #c9c9c9}
  .card-back{left:50px;top:562px;background:var(--black)}
  .front-waves{position:absolute;left:0;top:0;width:800px;height:456px}
  .brand{position:absolute;display:flex;align-items:center;gap:12px;
    font-family:"Michroma",sans-serif;color:var(--orange);font-size:24px;line-height:1.35;text-transform:uppercase}
  .brand-dot{width:30px;height:30px;border-radius:50%;background:var(--orange);flex:none}
  .front-brand{left:95px;top:150px;width:300px}
  .back-brand{left:145px;top:155px;width:300px}
  .divider{position:absolute;width:2px;background:var(--rule)}
  .front-divider{left:391px;top:73px;height:208px}
  .back-divider{left:440px;top:88px;height:218px;background:#777}
  .person{position:absolute;left:421px;top:88px}
  .person-name{font-family:"Michroma",sans-serif;color:var(--orange);font-size:25px;font-weight:700;letter-spacing:.5px}
  .person-title{font-family:"Michroma",sans-serif;color:var(--green);font-size:22px;margin-top:4px}
  .contacts{list-style:none;margin-top:24px}
  .contacts li{display:flex;align-items:center;gap:6px;color:var(--ink);font-size:19.5px;height:33px}
  .contacts svg{width:18px;height:18px;flex:none}
  .socials{position:absolute;right:50px;bottom:30px;display:flex;gap:17px}
  .social{width:36px;height:36px;border-radius:50%;border:2px solid var(--white)}
  .services{position:absolute;left:482px;top:92px}
  .services h2{font-family:"Michroma",sans-serif;color:var(--green);font-size:22px;font-weight:700;margin-bottom:12px}
  .services ul{list-style:none}
  .services li{color:var(--white);font-size:21px;height:44.5px;display:flex;align-items:center}
  .services li::before{content:"";width:7px;height:7px;border-radius:50%;background:var(--green);margin:0 15px 0 3px}
  .back-url{position:absolute;left:0;width:800px;top:368px;text-align:center;color:var(--white);font-size:24px;letter-spacing:2.6px}
</style>
</head>
<body>
  <section class="card card-front">
    <svg class="front-waves" viewBox="0 0 800 456" aria-hidden="true">
      <path d="M0 330 C120 410 250 440 330 436 C470 432 600 330 800 330 L800 456 L0 456Z" fill="var(--blue)"/>
      <path d="M0 285 C40 340 110 395 175 418 C105 400 40 360 0 320Z" fill="var(--orange)"/>
      <path d="M560 372 C650 330 730 310 800 313 L800 325 C720 322 640 345 560 372Z" fill="var(--orange)"/>
    </svg>
    <div class="brand front-brand"><span class="brand-dot"></span><span>Coral Tide<br>Fiesta DJ</span></div>
    <div class="divider front-divider"></div>
    <div class="person">
      <h1 class="person-name">DARIO VELLOZA</h1>
      <p class="person-title">TITLE</p>
      <ul class="contacts">
        <li><svg viewBox="0 0 20 20"><circle cx="10" cy="10" r="8.5" fill="none" stroke="var(--orange)" stroke-width="2"/><path d="M7 6l2 2-1 1.5c.7 1.3 1.5 2.1 2.8 2.8L12.3 11l2 2-1.3 1.3C9.5 14 6 10.5 5.7 7.3Z" fill="var(--orange)"/></svg>(555)014-7392</li>
        <li><svg viewBox="0 0 20 20"><circle cx="10" cy="10" r="8.5" fill="none" stroke="var(--orange)" stroke-width="2"/><rect x="5.5" y="7" width="9" height="6.5" fill="none" stroke="var(--orange)" stroke-width="1.5"/><path d="M5.5 7l4.5 4 4.5-4" fill="none" stroke="var(--orange)" stroke-width="1.5"/></svg>dario@coraltidefiestadj.example</li>
        <li><svg viewBox="0 0 20 20"><g fill="none" stroke="var(--orange)" stroke-width="1.6"><circle cx="10" cy="10" r="8.5"/><ellipse cx="10" cy="10" rx="3.8" ry="8.5"/><path d="M1.5 10h17M3 6h14M3 14h14"/></g></svg>www.coraltidefiestadj.example</li>
      </ul>
    </div>
    <div class="socials" aria-label="Social profiles @ctfiestadj">
      <span class="social"></span><span class="social"></span><span class="social"></span>
    </div>
  </section>

  <section class="card card-back">
    <div class="brand back-brand"><span class="brand-dot"></span><span>Coral Tide<br>Fiesta DJ</span></div>
    <div class="divider back-divider"></div>
    <div class="services">
      <h2>Services:</h2>
      <ul>
        <li>DJ</li>
        <li>Photo Booth</li>
        <li>Event Lighting</li>
        <li>LED Robot</li>
      </ul>
    </div>
    <p class="back-url">www.coraltidefiestadj.example</p>
  </section>
</body>
</html>
```